Logo / Etikettendesign
Zielgruppe
Renommierte Sektkellerei will neue Wege gehen. Es wird ein neues Produkt kreirt - ein Sekt - der nicht als Sekt wahrgenommen werden soll - sondern als "Lifestyle" Produkt.
Der neue Name des Produktes steht fest "Wolkenzauber"
Aufgabenstellung
Für den Namen "Wolkenzauber" wird ein neues Logo / Schriftzug / Wortbildmarke gesucht, das gleich auf einem Etikett platziert werden soll.
Es kann Perlmutt sein, Es kann bunt sein. schön wäre (nicht unbedingt erforderlich) wenn ein Kussmund dabei wäre. Aber bitte nicht an dem Mund aufhängen. Es kann auch gerne in die Nostalgische Ebene übergehen.
Die Flasche wird dunkelgrün sein.
Es soll später noch ein Rosé in transparenter Flasche dazu kommen.

```html
<!DOCTYPE html>
<html lang="de">
<head>
<meta charset="utf-8">
<title>Wolkenzauber – Jahrgangssekt Etikett</title>
<link rel="stylesheet" href="https://fonts.googleapis.com/css2?family=Cormorant+Garamond:wght@500;600&family=Montserrat:wght@400&display=swap">
<style>
  :root {
    --bottle-green-light: #053d1a;
    --bottle-green-dark: #010f06;
    --label-black: #1b1b1c;
    --label-edge: #0c0c0d;
    --gold-light: #f6e2d0;
    --gold-mid: #d9b293;
    --gold-deep: #a97e62;
    --band-ink: #2a2220;
  }
  html, body {
    margin: 0;
    padding: 0;
    width: 1200px;
    height: 1200px;
    overflow: hidden;
  }
  .canvas {
    width: 1200px;
    height: 1200px;
    background: linear-gradient(45deg, var(--bottle-green-light) 0%, #022712 45%, var(--bottle-green-dark) 100%);
  }
  .label {
    display: block;
    width: 1200px;
    height: 1200px;
  }
  .brand-name {
    font-family: "Cormorant Garamond", "Times New Roman", serif;
    font-weight: 600;
    font-size: 41px;
    letter-spacing: 1px;
  }
  .sort-line {
    font-family: "Montserrat", Arial, sans-serif;
    font-size: 8.5px;
    letter-spacing: 0.6px;
  }
  .taste {
    font-family: "Cormorant Garamond", "Times New Roman", serif;
    font-weight: 500;
    font-size: 15px;
  }
</style>
</head>
<body>
<main class="canvas">
  <svg class="label" viewBox="0 0 800 800" xmlns="http://www.w3.org/2000/svg">
    <defs>
      <linearGradient id="goldGradient" x1="0" y1="0" x2="1" y2="1">
        <stop offset="0" stop-color="var(--gold-light)"/>
        <stop offset="0.5" stop-color="var(--gold-mid)"/>
        <stop offset="1" stop-color="var(--gold-deep)"/>
      </linearGradient>
      <linearGradient id="titleGradient" x1="0" y1="0" x2="0" y2="1">
        <stop offset="0" stop-color="#fbeee2"/>
        <stop offset="1" stop-color="#dcb497"/>
      </linearGradient>
      <linearGradient id="panelGradient" x1="0" y1="0" x2="1" y2="0">
        <stop offset="0" stop-color="#111112"/>
        <stop offset="0.5" stop-color="#2a2a2b"/>
        <stop offset="1" stop-color="#111112"/>
      </linearGradient>
      <linearGradient id="bandGradient" x1="0" y1="0" x2="1" y2="0">
        <stop offset="0" stop-color="#c89a78"/>
        <stop offset="0.5" stop-color="#f8e6d6"/>
        <stop offset="1" stop-color="#c89a78"/>
      </linearGradient>
      <radialGradient id="bubbleGlow" cx="0.5" cy="0.45" r="0.55">
        <stop offset="0" stop-color="#e8c9ad" stop-opacity="0.55"/>
        <stop offset="1" stop-color="#e8c9ad" stop-opacity="0"/>
      </radialGradient>
    </defs>

    <!-- shield outline -->
    <path class="shield-edge" fill="var(--label-edge)"
      d="M400,170 Q460,176 506,208 L520,198 Q575,216 612,244 C618,330 612,420 582,502 C546,588 470,624 400,642 C330,624 254,588 218,502 C188,420 182,330 188,244 Q225,216 280,198 L294,208 Q340,176 400,170 Z"/>
    <!-- fine gold border band -->
    <path class="shield-border" fill="none" stroke="url(#goldGradient)" stroke-width="7" stroke-dasharray="1.2 1.3"
      d="M400,180 Q458,186 505,218 L519,209 Q568,225 601,250 C606,332 601,418 572,496 C538,578 468,612 400,630 C332,612 262,578 228,496 C199,418 194,332 199,250 Q232,225 281,209 L295,218 Q342,186 400,180 Z"/>
    <!-- black panel -->
    <path class="shield-panel" fill="url(#panelGradient)"
      d="M400,190 Q456,196 503,228 L517,220 Q562,235 592,257 C596,334 591,416 563,491 C531,569 464,601 400,619 C336,601 269,569 237,491 C209,416 204,334 208,257 Q238,235 283,220 L297,228 Q344,196 400,190 Z"/>
    <!-- inner gold hairline -->
    <path class="shield-hairline" fill="none" stroke="var(--gold-mid)" stroke-width="0.9"
      d="M400,198 Q454,204 501,236 L515,228 Q556,242 584,262 C588,336 583,414 556,487 C525,562 461,593 400,611 C339,593 275,562 244,487 C217,414 212,336 216,262 Q244,242 285,228 L299,236 Q346,204 400,198 Z"/>

    <!-- kiss mouth formed of bubbles -->
    <g role="img" aria-label="Kussmund aus goldenen Sektperlen mit aufsteigender Perlenspur">
      <ellipse cx="398" cy="258" rx="66" ry="44" fill="url(#bubbleGlow)"/>
      <ellipse cx="396" cy="320" rx="14" ry="28" fill="url(#bubbleGlow)"/>
    </g>

    <text class="brand-name" x="400" y="416" text-anchor="middle" fill="url(#titleGradient)">WOLKENZAUBER</text>

    <line class="divider" x1="258" y1="442" x2="340" y2="442" stroke="var(--gold-deep)" stroke-width="0.8"/>
    <line class="divider" x1="460" y1="442" x2="542" y2="442" stroke="var(--gold-deep)" stroke-width="0.8"/>
    <text class="sort-line" x="400" y="445" text-anchor="middle" fill="var(--gold-light)">Jahrgangssekt</text>

    <!-- flourish -->
    <rect role="img" aria-label="Geschwungenes goldenes Zierornament" x="315" y="488" width="170" height="40" rx="20"
      fill="var(--gold-mid)" fill-opacity="0.18"/>

    <!-- bottom band -->
    <path class="taste-band" fill="url(#bandGradient)"
      d="M292,540 Q400,562 508,540 Q480,580 430,602 Q412,610 400,612 Q388,610 370,602 Q320,580 292,540 Z"/>
    <text class="taste" x="400" y="586" text-anchor="middle" fill="var(--band-ink)">trocken</text>
  </svg>
</main>
</body>
</html>
```